LedgerNook Project
LedgerNook
Project: LedgerNook Project
LedgerNook Project - Financial Services
Creative Brief
Bright & Fun-filled
Peter Halvik
President
Leave blank
peter@ledgernook.example
www.ledgernook.example
The front should be white with logo, my name, cell phone, email address, and website. Leave address blank because there is no physical address at the moment. List these services with bullet point. (accounting, bookkeeping, and payroll) Please make sure the design meet GlossPrint silk laminate with spot uv because I plan to use them to print in the future. Check link: http://www.glossprint.example/Business-Cards/Silk-Business-Cards-with-Spot-UV-and-Rounded-Corners
I want the back to be a solid color with logo. Check link for what I am looking for: http://www.glossprint.example/Inspiration-Gallery#/gallery/img/images_M.jpg

```html
<!DOCTYPE html>
<html lang="en">
<head>
<meta charset="utf-8">
<title>LedgerNook Business Card</title>
<link href="https://fonts.googleapis.com/css2?family=Open+Sans:wght@400;600;700&display=swap" rel="stylesheet">
<style>
  :root {
    --page-bg: #efe6d6;
    --card-white: #ffffff;
    --card-grey: #ececec;
    --brand-blue: #3a8fd0;
    --brand-navy: #0d2a44;
    --text-light: #ffffff;
    --text-dark: #14304d;
  }
  html, body {
    margin: 0;
    width: 1200px;
    height: 935px;
    overflow: hidden;
    background: var(--page-bg);
    font-family: "Open Sans", Arial, sans-serif;
  }
  .card {
    position: absolute;
    left: 193px;
    top: 235px;
    width: 815px;
    height: 465px;
    border-radius: 38px;
    overflow: hidden;
    background: linear-gradient(135deg, var(--card-white) 40%, var(--card-grey) 100%);
    box-shadow: 0 6px 18px rgba(0,0,0,0.18);
  }
  .card-shapes {
    position: absolute;
    inset: 0;
  }
  .holder {
    position: absolute;
    left: 46px;
    top: 20px;
    color: var(--text-light);
  }
  .holder-name {
    margin: 0;
    font-size: 28px;
    font-weight: 700;
    line-height: 1.3;
  }
  .holder-title {
    margin: 0;
    font-size: 17px;
    font-weight: 400;
  }
  .contact {
    position: absolute;
    left: 46px;
    top: 292px;
    margin: 0;
    padding: 0;
    list-style: none;
    color: var(--text-light);
    font-size: 20px;
    line-height: 26px;
  }
  .contact strong { font-weight: 700; }
  .brand {
    position: absolute;
    left: 470px;
    top: 92px;
    width: 320px;
    display: flex;
    flex-direction: column;
    align-items: center;
    gap: 54px;
  }
  .brand-mark {
    width: 96px;
    height: 110px;
    background: var(--brand-blue);
  }
  .brand-name {
    font-size: 44px;
    font-weight: 700;
    line-height: 1;
    color: var(--text-dark);
    letter-spacing: -1px;
    white-space: nowrap;
  }
</style>
</head>
<body>
  <div class="card">
    <svg class="card-shapes" width="815" height="465" viewBox="0 0 815 465">
      <path d="M0 0 H432 Q300 232 458 465 H0 Z" fill="var(--brand-navy)"/>
      <path d="M0 0 H392 Q270 240 440 465 H0 Z" fill="var(--brand-blue)"/>
    </svg>

    <div class="holder">
      <p class="holder-name">Peter Halvik</p>
      <p class="holder-title">President</p>
    </div>

    <ul class="contact">
      <li>xxxxxxxxxxxxxxxxx,</li>
      <li>xxxxxxxxxxxxxxxxxxxxxx.</li>
      <li><strong>Cell :</strong> 555-014-2287</li>
      <li><strong>Email :</strong> peter@ledgernook.example</li>
      <li><strong>Web :</strong> www.ledgernook.example</li>
    </ul>

    <div class="brand">
      <span class="brand-mark"></span>
      <span class="brand-name">LedgerNook</span>
    </div>
  </div>
</body>
</html>
```